Website and business logo needed

Organisation for the community providing dispute resolution services, peace building.

I'd like calm colours, a strong simple logo symbolising collaboration, peace and cohesion. Needs to convey that message in a symbol.

We provide different types of services so we do mediation, and training and provide publications and research. It's community based and designed to work with the community for the community.

Industry/Entity Type

Training

Contact Information for Business Card

Quiet Harbour - Institute for Neighbourhood and Conflict Settlement
communication skills, mediation, facilitation, conflict coaching, education, training, research
PO Box 7416
South Brisbane
0418 627 903

Requirements
Must have
• Logo
Calm but strong colours

```html
<!DOCTYPE html>
<html lang="en">
<head>
<meta charset="utf-8">
<title>Quiet Harbour – Business Cards</title>
<link rel="stylesheet" href="https://fonts.googleapis.com/css2?family=Fira+Sans:wght@400;600&display=swap">
<style>
  :root {
    --backdrop: #e8e5e0;
    --card: #fbfbfb;
    --ink: #141414;
    --sun: #ebc20a;
    --rule: #1a1a1a;
    --shadow: rgba(0, 0, 0, 0.14);
  }
  * { box-sizing: border-box; margin: 0; padding: 0; }
  html, body {
    width: 1200px;
    height: 880px;
    overflow: hidden;
    background: var(--backdrop);
    font-family: "Fira Sans", Arial, sans-serif;
    color: var(--ink);
  }
  .canvas {
    position: relative;
    width: 1200px;
    height: 880px;
  }
  .card {
    position: absolute;
    width: 580px;
    height: 330px;
    background: var(--card);
    box-shadow: 0 6px 18px var(--shadow);
  }
  .card--back { left: 560px; top: 100px; }
  .card--front { left: 60px; top: 450px; }

  .brand-dot {
    display: block;
    border-radius: 50%;
    background: var(--sun);
  }
  .brand-name {
    font-weight: 600;
    color: var(--ink);
    letter-spacing: 0.2px;
    white-space: nowrap;
  }

  /* front */
  .front-brand {
    position: absolute;
    top: 42px;
    left: 0;
    right: 0;
    display: flex;
    flex-direction: column;
    align-items: center;
  }
  .front-brand .brand-dot { width: 112px; height: 112px; margin-bottom: 16px; }
  .front-brand .brand-name { font-size: 32px; line-height: 1; }
  .front-brand .tagline {
    font-size: 11px;
    margin-top: 6px;
    letter-spacing: 0.1px;
    white-space: nowrap;
  }
  .services {
    position: absolute;
    left: 22px;
    right: 22px;
    bottom: 32px;
    display: flex;
    justify-content: space-between;
    list-style: none;
    font-size: 11.5px;
    white-space: nowrap;
  }
  .services li { flex: 0 0 auto; }
  .services li + li::before {
    content: "•";
    margin-right: 4px;
  }

  /* back */
  .back-brand {
    position: absolute;
    left: 40px;
    top: 70px;
    width: 180px;
    display: flex;
    flex-direction: column;
    align-items: center;
  }
  .back-brand .brand-dot { width: 104px; height: 104px; margin-bottom: 14px; }
  .back-brand .brand-name { font-size: 24px; line-height: 1; }
  .divider {
    position: absolute;
    left: 242px;
    top: 58px;
    width: 2px;
    height: 190px;
    background: var(--rule);
  }
  .contact {
    position: absolute;
    left: 264px;
    top: 122px;
    font-style: normal;
    font-size: 22px;
    line-height: 1.25;
    white-space: nowrap;
  }
</style>
</head>
<body>
<main class="canvas">

  <section class="card card--back" aria-label="Business card, back">
    <div class="back-brand">
      <span class="brand-dot" aria-hidden="true"></span>
      <span class="brand-name">Quiet Harbour</span>
    </div>
    <span class="divider" aria-hidden="true"></span>
    <address class="contact">
      PO Box 7416 South Brisbane<br>
      0418 627 903
    </address>
  </section>

  <section class="card card--front" aria-label="Business card, front">
    <div class="front-brand">
      <span class="brand-dot" aria-hidden="true"></span>
      <span class="brand-name">Quiet Harbour</span>
      <span class="tagline">Institute for Neighbourhood and Conflict Settlement</span>
    </div>
    <ul class="services">
      <li>communication skills</li>
      <li>mediation</li>
      <li>facilitation</li>
      <li>conflict coaching</li>
      <li>education</li>
      <li>training</li>
      <li>research</li>
    </ul>
  </section>

</main>
</body>
</html>
```